Upscale business cards needed for family office

We would like professional business cards created for employees of our family office. Relatively simple and straightforward, but also with a unique element to set them apart. Probably stick with neutral and simple colors that mesh well with the colors in the logo. We need space for the traditional elements, including name, title, address, email/phone number.

Industry/Entity Type

Business

Contact Information for Business Card

Space for name, title, phone number, email, address

```html
<!DOCTYPE html>
<html lang="en">
<head>
<meta charset="UTF-8">
<title>R&amp;T Business Cards</title>
<link rel="stylesheet" href="https://fonts.googleapis.com/css2?family=Roboto:wght@400;500&family=Saira+Semi+Condensed:wght@600&display=swap">
<style>
  :root {
    --backdrop: #e6e7e9;
    --card-paper: #f4f4f2;
    --brand-navy: #2d5591;
    --brand-aqua: #1b8fbf;
    --brand-grey: #5f5f5f;
    --arc-grey: #58595b;
    --text-light: #ffffff;
    --text-soft: #dfe6f2;
  }
  * { box-sizing: border-box; margin: 0; padding: 0; }
  html, body {
    width: 1200px; height: 1095px; overflow: hidden;
    background: var(--backdrop);
    font-family: "Roboto", Arial, sans-serif;
  }
  .stage { position: relative; width: 1200px; height: 1095px; }
  .card {
    position: absolute; left: 270px; width: 660px; height: 390px;
    background: var(--card-paper); overflow: hidden;
    box-shadow: 0 3px 10px rgba(0,0,0,0.12);
  }
  .card--front { top: 120px; }
  .card--back { top: 545px; }
  .card__stripe {
    position: absolute; left: 0; right: 0; bottom: 0; height: 9px;
    background: var(--brand-aqua);
  }
  .brand {
    position: absolute; display: flex; align-items: center; gap: 12px;
    color: var(--brand-grey); font-family: "Roboto", Arial, sans-serif;
    font-weight: 400; letter-spacing: 1px;
  }
  .brand__square { background: var(--brand-navy); }
  .card--front .brand { left: 0; right: 0; top: 130px; justify-content: center; font-size: 64px; }
  .card--front .brand__square { width: 26px; height: 26px; }
  .card--back .brand { left: 52px; top: 150px; font-size: 66px; }
  .card--back .brand__square { width: 26px; height: 26px; }
  .back-shape { position: absolute; inset: 0; }
  .holder {
    position: absolute; left: 336px; top: 76px; color: var(--text-light);
  }
  .holder__name {
    font-family: "Saira Semi Condensed", "Arial Narrow", sans-serif;
    font-weight: 600; font-size: 25px; line-height: 1;
  }
  .holder__title { margin-top: 10px; font-size: 15px; color: var(--text-soft); }
  .contact { position: absolute; left: 336px; top: 183px; list-style: none; color: var(--text-light); }
  .contact__item { display: flex; align-items: center; gap: 12px; font-size: 17px; line-height: 24px; }
  .contact__icon { width: 14px; height: 14px; fill: var(--text-light); }
  .address {
    position: absolute; left: 336px; top: 269px; font-size: 17px; line-height: 25px;
    color: var(--text-light); font-style: normal;
  }
</style>
</head>
<body>
<main class="stage">
  <section class="card card--front" aria-label="Business card front">
    <div class="brand"><span class="brand__square"></span><span class="brand__name">R&amp;T</span></div>
    <div class="card__stripe"></div>
  </section>

  <section class="card card--back" aria-label="Business card back">
    <svg class="back-shape" width="660" height="390" viewBox="0 0 660 390">
      <path d="M 210 0 Q 340 200 235 390" fill="none" stroke="var(--arc-grey)" stroke-width="7"/>
      <path d="M 230 0 Q 360 200 248 390 L 660 390 L 660 0 Z" fill="var(--brand-navy)"/>
    </svg>
    <div class="brand"><span class="brand__square"></span><span class="brand__name">R&amp;T</span></div>
    <div class="holder">
      <h1 class="holder__name">Your Good Name</h1>
      <p class="holder__title">Managing Director</p>
    </div>
    <ul class="contact">
      <li class="contact__item">
        <svg class="contact__icon" viewBox="0 0 16 16"><path d="M2 5 Q8 1 14 5 L12 7 L10 6 L10 5 Q8 4 6 5 L6 6 L4 7 Z M3 9 H13 V13 H3 Z"/></svg>
        <span>+00 111 222 3333</span>
      </li>
      <li class="contact__item">
        <svg class="contact__icon" viewBox="0 0 16 16"><path d="M1 3 H15 V13 H1 Z M2 4 L8 9 L14 4" stroke="var(--brand-navy)" stroke-width="1"/></svg>
        <span>yourname@yourwebsite.com</span>
      </li>
      <li class="contact__item">
        <svg class="contact__icon" viewBox="0 0 16 16"><circle cx="8" cy="8" r="6.5" fill="none" stroke="var(--text-light)" stroke-width="1.4"/><path d="M1.5 8 H14.5 M8 1.5 Q4 8 8 14.5 M8 1.5 Q12 8 8 14.5" fill="none" stroke="var(--text-light)" stroke-width="1.2"/></svg>
        <span>www.yourwebsite.com</span>
      </li>
    </ul>
    <address class="address">Your Long Commercial or business<br>address in 2 line</address>
  </section>
</main>
</body>
</html>
```